Flu Brochure- brief and easy-to-read

A team of health educators is looking to design a brochure on what Americans need to "know and do" when it comes to flu season. All copy and images will be provided.

The brochure needs to be an 8.5 x 11 inch bi-fold design.

I am only able to upload up to 5 files. So, additional images will have to sent via dropbox or some other mechanism.

Target Market(s)

The audience is vast, but the content and design need to be simple and engaging.

Industry/Entity Type

Health

Requirements
Must have
• Must Have:
- Clear and Simple, Easy-to-read and Understand and Act on- should be very focused on what the consumer should do about taking care of themselves when it comes to the flu.

We will provide all of the copy for the brochure design. We will also provide photographs for the project.

Captions for photographs that support the key message.

Should Not Have:
- x reverse print- e.g., no white font on a black background
x fancy fonts or heavy use of italics
x use of all capitals
x no full justification
x no use of drop caps

Must be multicultural as well.

```html
<!DOCTYPE html>
<html lang="en">
<head>
<meta charset="utf-8">
<title>Flu Season: Know, Prevent, Protect, Treat</title>
<link rel="stylesheet" href="https://fonts.googleapis.com/css2?family=Anton&family=Archivo+Narrow:wght@700&family=Questrial&display=swap">
<style>
  :root {
    --cyan: #29abe2;
    --navy: #1f3b8f;
    --ink: #000000;
    --paper: #ffffff;
    --rule: #c8c8c8;
  }
  * { margin: 0; padding: 0; box-sizing: border-box; }
  html, body { width: 1200px; height: 1085px; overflow: hidden; background: var(--paper); }
  .brochure {
    position: relative; width: 1200px; height: 1085px;
    font-family: "Questrial", "Century Gothic", sans-serif; color: var(--ink);
  }
  .fold { position: absolute; left: 594px; top: 0; height: 1085px; border-left: 2px dashed var(--rule); }
  .titles { position: absolute; left: 0; top: 0; width: 1200px; height: 1085px; }
  .titles .word { font-family: "Anton", "Impact", sans-serif; fill: var(--ink); }
  .titles .num { font-family: "Questrial", "Century Gothic", sans-serif; fill: var(--cyan); stroke: var(--cyan); stroke-width: 2px; }
  .block { position: absolute; white-space: nowrap; }
  .lead { font-size: 25px; line-height: 28px; }
  .lead.small { font-size: 20px; line-height: 24px; }
  .centered { text-align: center; color: var(--navy); font-size: 16.5px; line-height: 20px; }
  .centered .or { color: var(--ink); font-family: "Archivo Narrow", sans-serif; font-weight: 700; }
  .steps {
    list-style: none; counter-reset: step; color: var(--navy);
    font-size: 15.5px; line-height: 19.7px;
  }
  .steps li { counter-increment: step; position: relative; padding-left: 22px; }
  .steps li::before { content: counter(step) "."; position: absolute; left: 0; }
  .steps b { font-family: "Archivo Narrow", "Arial Narrow", sans-serif; font-weight: 700; font-size: 16.5px; }
  .callout {
    position: absolute; background: var(--cyan); color: var(--paper); text-align: center;
    font-family: "Archivo Narrow", "Arial Narrow", sans-serif; font-weight: 700;
  }
  .callout .plain { font-family: "Questrial", sans-serif; font-weight: 400; }
</style>
</head>
<body>
<main class="brochure">
  <div class="fold" aria-hidden="true"></div>

  <svg class="titles" viewBox="0 0 1200 1085" aria-label="Know, Warning signs, Prevent, The shot, Protect, Treat">
    <text class="num" x="22" y="235" font-size="83" textLength="54" lengthAdjust="spacingAndGlyphs">1.</text>
    <text class="word" x="82" y="235" font-size="116" textLength="353" lengthAdjust="spacingAndGlyphs">KNOW</text>
    <text class="word" x="25" y="370" font-size="37" textLength="330" lengthAdjust="spacingAndGlyphs">WARNING SIGNS:</text>
    <text class="num" x="18" y="660" font-size="83" textLength="68" lengthAdjust="spacingAndGlyphs">2.</text>
    <text class="word" x="90" y="660" font-size="116" textLength="447" lengthAdjust="spacingAndGlyphs">PREVENT</text>
    <text class="word" x="25" y="838" font-size="38" textLength="190" lengthAdjust="spacingAndGlyphs">THE SHOT:</text>
    <text class="num" x="612" y="243" font-size="83" textLength="70" lengthAdjust="spacingAndGlyphs">3.</text>
    <text class="word" x="685" y="243" font-size="117" textLength="482" lengthAdjust="spacingAndGlyphs">PROTECT</text>
    <text class="num" x="612" y="577" font-size="83" textLength="70" lengthAdjust="spacingAndGlyphs">4.</text>
    <text class="word" x="687" y="577" font-size="116" textLength="306" lengthAdjust="spacingAndGlyphs">TREAT</text>
  </svg>

  <!-- Know -->
  <p class="block lead" style="left:22px; top:248px;">common complaints for flu:</p>
  <p class="block centered" style="left:40px; width:560px; top:282px;">FEVER, COUGH, SORE THROAT, RUNNY <span class="or">or</span> STUFFY NOSE,<br>HEADACHES, BODY ACHES, CHILLS, BEING TIRED</p>
  <p class="block centered" style="left:57px; width:560px; top:390px;">HARD TIME BREATHING <span class="or">or</span> SHORT OF BREATH<br>PAIN <span class="or">or</span> PRESSURE IN THE CHEST <span class="or">or</span> STOMACH<br>FEELING DIZZY ALL OF THE SUDDEN<br>BECOMING CONFUSED</p>
  <p class="callout" style="left:20px; top:490px; width:559px; height:42px; line-height:42px; font-size:19px;">If you have ANY of the warning signs, contact your doctor!</p>

  <!-- Prevent -->
  <p class="block lead small" style="left:20px; top:668px;">How can I keep me and my family from getting the flu?</p>
  <ol class="block steps" style="left:42px; top:696px;">
    <li>Be sure everyone <b>6 MONTHS</b> and <b>OLDER</b> gets the <b>FLU SHOT</b>.</li>
    <li>You can get the <b>FLU SHOT</b> through a <b>NEEDLE</b> or a &nbsp;.</li>
    <li><b>THE FLU SHOT HELPS PROTECT YOU AGAINST THE THREE MOST<br>COMMON TYPES OF FLU.</b></li>
  </ol>
  <ol class="block steps" style="left:42px; top:857px;">
    <li>Does <b>NOT</b> give you the flu.</li>
    <li>Is <b>VERY</b> IMPORTANT for pregnant women.</li>
    <li><b>YOU DON’T NEED A PRESCRIPTION FOR IT!</b></li>
  </ol>

  <!-- Protect -->
  <p class="block lead" style="left:612px; top:247px;">How do I protect my family?</p>
  <ol class="block steps" style="left:630px; top:279px;">
    <li><b>STAY AWAY</b> from sick people.</li>
    <li><b>WASH YOUR HANDS</b> with <b>SOAP</b> and <b>WATER</b> or <b>HAND SANITIZER</b><br>when you eat, cough or go to the bathroom.</li>
    <li><b>TRY NOT TO TOUCH</b> eyes, nose, or mouth because that is<br>how you catch the flu.</li>
    <li><b>COUGH</b> or <b>SNEEZE</b> into your sleeve or cover your nose<br>and mouth with a tissue.</li>
    <li><b>THROW THE TISSUE IN THE TRASH!</b></li>
  </ol>

  <!-- Treat -->
  <p class="block lead small" style="left:612px; top:580px;">What if someone has the flu?</p>
  <div class="callout" style="left:607px; top:607px; width:574px; height:83px; padding-top:9px; font-size:18px; line-height:22px;">
    <p class="plain">If you think someone in your family has the flu, call your doctor.</p>
    <p>Ask if they need to be seen.</p>
    <p>Ask your doctor about flu medicine.</p>
  </div>
  <p class="block lead small" style="left:614px; top:698px;">If your doctor tells you to treat yourself...</p>
  <ol class="block steps" style="left:630px; top:734px;">
    <li><b>STAY HOME</b> and <b>REST</b> – don’t spread your germs to others!</li>
    <li><b>TAKE MEDICINE FOR FEVER</b>, such as acetaminophen (Tempira)<br>or ibuprofen (Ibrulin, Achelo, Nuvrelle)</li>
    <li><b>DO NOT TAKE ASPIRIN FOR FEVER.</b></li>
    <li><b>DRINK</b> 6-8 big glasses of water, juice, or sport drink (like Sipwell Sport,<br>Quenchra) <b>EVERYDAY</b>.</li>
    <li><b>IF AROUND OTHER PEOPLE, WEAR A MASK.</b></li>
  </ol>
</main>
</body>
</html>
```